e-commerce store for sport clothing online store "baseball merchandise "web application...

I want to design a UX/UI for my web application website for the online store I will provide you with the following:
1. screen shots of the initial design for the pages>
2. the logo files.
3. The brand guideline file.

the provided files (screen shots) is guideline I want to see CREATIVITY with the UX/UI DESIGN.
PS. PLEASE FOLLOW THE BRANDGUIDE LINE CAREFULLY SPECIALLY THE TYPOGRAPHY & THE COLOR CODES.

PLEASE VISIT THIS WEBSITE brightpin.lumar-qt.com to see more for the screens.

```html
<!DOCTYPE html>
<html lang="en">
<head>
<meta charset="UTF-8">
<title>Fieldstar Store – Home</title>
<link href="https://fonts.googleapis.com/css2?family=Titillium+Web:wght@400;600;700&family=Archivo+Black&display=swap" rel="stylesheet">
<style>
  :root{
    --navy:#13254a;
    --ink:#111111;
    --cream:#fdf6d8;
    --sun:#ffcf1f;
    --khaki:#998b60;
    --soft-grey:#d9d9d9;
    --accent-red:#b3132e;
    --muted:#b5b5b5;
    --white:#ffffff;
    --teal:#4fb3bf;
    --heading:#2b2b2b;
    --gold:#f1c232;
  }
  *{box-sizing:border-box;margin:0;padding:0}
  html,body{width:1079px;height:1200px;overflow:hidden;background:var(--white)}
  body{font-family:"Titillium Web",sans-serif;color:var(--ink);position:relative}
  .stage{position:relative;width:1079px;height:1200px}

  /* header */
  .site-header{position:absolute;left:0;top:0;width:1079px;height:120px}
  .brand-name{position:absolute;left:38px;top:42px;display:flex;align-items:center;gap:8px;
    font-weight:700;font-size:24px;color:var(--navy);letter-spacing:.5px}
  .brand-dot{width:14px;height:14px;border-radius:50%;background:var(--navy)}
  .main-nav{position:absolute;left:490px;top:38px;display:flex;align-items:center}
  .nav-link{font-size:17px;color:var(--ink);text-decoration:none;margin-right:38px}
  .nav-link.is-active{background:var(--navy);color:var(--white);font-weight:600;
    width:110px;height:40px;border-radius:5px;display:flex;align-items:center;justify-content:center;margin-right:20px}
  .header-icons{position:absolute;left:893px;top:50px;display:flex;gap:34px}

  /* hero */
  .hero{position:absolute;left:0;top:120px;width:1079px;height:411px;background:var(--cream);overflow:hidden}
  .hero-corner{position:absolute;left:-70px;top:-110px;width:180px;height:214px;border-radius:50%;background:var(--sun)}
  .hero-badge{position:absolute;left:130px;top:30px;width:114px;height:114px;border-radius:50%;
    background:#0d0d0d;border:4px solid var(--teal);display:flex;flex-direction:column;align-items:center;justify-content:center;
    font-family:"Archivo Black",sans-serif;color:var(--gold);font-size:22px;line-height:1.2}
  .hero-visual{position:absolute;left:316px;top:50px;width:330px;height:361px;border-radius:165px 165px 0 0;
    background:radial-gradient(ellipse at 50% 35%,#f3d2b8 0%,#e86b4d 45%,#f6b431 80%,rgba(253,246,216,0) 100%)}
  .hero-title{position:absolute;right:158px;top:98px;text-align:right;font-family:"Archivo Black",sans-serif;color:var(--heading)}
  .hero-title .line{display:block;font-size:43px;line-height:52px}
  .hero-title .sub{display:block;font-size:18px;line-height:28px;margin-top:2px}
  .hero-cta{position:absolute;left:721px;top:274px;width:201px;height:60px;border-radius:10px;background:#0b0b0b;
    color:var(--gold);font-family:"Archivo Black",sans-serif;font-size:27px;display:flex;align-items:center;justify-content:center;
    box-shadow:0 4px 8px rgba(0,0,0,.3)}

  /* search panel */
  .search-panel{position:absolute;left:153px;top:475px;width:772px;height:113px;border-radius:12px;background:var(--khaki);
    box-shadow:0 4px 6px rgba(0,0,0,.2);color:var(--white)}
  .search-field{position:absolute;top:32px}
  .field-label{display:block;font-size:17px;font-weight:400}
  .field-value{display:block;font-size:17px;font-weight:700;margin-top:12px}
  .search-button{position:absolute;left:570px;top:33px;width:180px;height:43px;border-radius:8px;background:var(--soft-grey);
    color:var(--ink);font-weight:700;font-size:17px;display:flex;align-items:center;justify-content:center}

  /* catalogue */
  .category-title{position:absolute;left:38px;top:686px;font-size:30px;font-weight:700}
  .product-card{position:absolute;top:761px;width:290px;height:375px;border-radius:16px;background:var(--white);
    box-shadow:0 2px 10px rgba(0,0,0,.14)}
  .product-image{position:absolute;left:30px;top:20px;width:230px;height:180px;border-radius:12px}
  .product-image.cap{background:radial-gradient(ellipse at 50% 55%,#1c1c1c 0%,#2c2c2c 50%,rgba(255,255,255,0) 72%)}
  .product-image.shirt{background:radial-gradient(ellipse at 50% 50%,#ffffff 0%,#2a8fd6 45%,#111 62%,rgba(255,255,255,0) 75%)}
  .product-name{position:absolute;left:19px;top:222px;font-size:18px;font-weight:600}
  .size-picker{position:absolute;right:30px;top:224px;display:flex;align-items:center;gap:10px;font-weight:700;font-size:13px}
  .size-picker .is-selected{background:var(--accent-red);color:var(--white);width:22px;height:22px;border-radius:3px;
    display:flex;align-items:center;justify-content:center;font-size:15px}
  .product-desc{position:absolute;left:20px;top:270px;width:251px;font-size:7px;line-height:11px;color:var(--muted);text-align:justify}
  .product-foot{position:absolute;left:20px;top:330px;width:250px;height:26px;display:flex;align-items:center}
  .price{font-size:17px;font-weight:700;width:80px}
  .qty{display:flex;align-items:center;gap:12px;font-size:18px;font-weight:700}
  .qty-box{width:24px;height:24px;border:1px solid #ccc;display:flex;align-items:center;justify-content:center;font-size:16px}
  .add-cart{margin-left:auto}
</style>
</head>
<body>
<div class="stage">

  <header class="site-header">
    <div class="brand-name"><span class="brand-dot"></span>FIELDSTAR</div>
    <nav class="main-nav">
      <a class="nav-link is-active" href="#">Home</a>
      <a class="nav-link" href="#">Shop</a>
      <a class="nav-link" href="#">Brand</a>
      <a class="nav-link" href="#">Help</a>
    </nav>
    <div class="header-icons">
      <svg width="18" height="18" viewBox="0 0 18 18" aria-label="Account"><circle cx="9" cy="5" r="4.5" fill="#111"/><path d="M1 18c0-5 3.5-7 8-7s8 2 8 7z" fill="#111"/></svg>
      <svg width="18" height="18" viewBox="0 0 18 18" aria-label="Cart"><path d="M0 2h3l2.5 9h9.5l2-7H5" fill="none" stroke="#111" stroke-width="2"/><path d="M5 5h11l-1.6 5.5H6.5z" fill="#111"/><circle cx="7" cy="15.5" r="1.6" fill="#111"/><circle cx="14" cy="15.5" r="1.6" fill="#111"/></svg>
    </div>
  </header>

  <section class="hero">
    <div class="hero-corner"></div>
    <div class="hero-badge"><span>75%</span><span>OFF</span></div>
    <div class="hero-visual" role="img" aria-label="Smiling shopper in a red sun hat holding colourful shopping bags and a phone"></div>
    <h1 class="hero-title">
      <span class="line">ONLINE</span>
      <span class="line">SHOPPING</span>
      <span class="sub">END OFF SEASON SALE</span>
    </h1>
    <div class="hero-cta">BUY NOW</div>
  </section>

  <form class="search-panel">
    <div class="search-field" style="left:27px"><span class="field-label">Location</span><span class="field-value">Port Avel, LK</span></div>
    <div class="search-field" style="left:184px"><span class="field-label">Date</span><span class="field-value">2022-12-12</span></div>
    <div class="search-field" style="left:331px"><span class="field-label">Year</span><span class="field-value">Port Avel, LK</span></div>
    <div class="search-field" style="left:462px"><span class="field-label">Type</span><span class="field-value">T Shirt</span></div>
    <div class="search-button">Search</div>
  </form>

  <h2 class="category-title">Catogory 01</h2>

  <article class="product-card" style="left:80px">
    <div class="product-image cap" role="img" aria-label="Black baseball cap with white striped brim"></div>
    <h3 class="product-name">Korvane Cap</h3>
    <div class="size-picker"><span>S</span><span class="is-selected">M</span><span>L</span></div>
    <p class="product-desc">Soft cotton twill with a curved brim and an adjustable strap at the back. Breathable panels keep you cool through every inning, and the clean stitched finish looks right in the stands, at practice, on the road or out on the street with friends after the game.</p>
    <div class="product-foot">
      <span class="price">300 $</span>
      <div class="qty"><span>−</span><span class="qty-box">1</span><span>+</span></div>
      <svg class="add-cart" width="16" height="16" viewBox="0 0 18 18" aria-label="Add to cart"><path d="M0 2h3l2.5 9h9.5l2-7H5" fill="none" stroke="#b3132e" stroke-width="2"/><path d="M5 5h11l-1.6 5.5H6.5z" fill="#b3132e"/><circle cx="7" cy="15.5" r="1.6" fill="#b3132e"/><circle cx="14" cy="15.5" r="1.6" fill="#b3132e"/></svg>
    </div>
  </article>

  <article class="product-card" style="left:394px">
    <div class="product-image shirt" role="img" aria-label="White, blue and black sports jersey"></div>
    <h3 class="product-name">BB T - Shirt</h3>
    <div class="size-picker"><span>S</span><span class="is-selected">M</span><span>L</span></div>
    <p class="product-desc">Soft cotton twill with a curved brim and an adjustable strap at the back. Breathable panels keep you cool through every inning, and the clean stitched finish looks right in the stands, at practice, on the road or out on the street with friends after the game.</p>
    <div class="product-foot">
      <span class="price">899 $</span>
      <div class="qty"><span>−</span><span class="qty-box">1</span><span>+</span></div>
      <svg class="add-cart" width="16" height="16" viewBox="0 0 18 18" aria-label="Add to cart"><path d="M0 2h3l2.5 9h9.5l2-7H5" fill="none" stroke="#b3132e" stroke-width="2"/><path d="M5 5h11l-1.6 5.5H6.5z" fill="#b3132e"/><circle cx="7" cy="15.5" r="1.6" fill="#b3132e"/><circle cx="14" cy="15.5" r="1.6" fill="#b3132e"/></svg>
    </div>
  </article>

  <article class="product-card" style="left:708px">
    <div class="product-image cap" role="img" aria-label="Black baseball cap with white striped brim"></div>
    <h3 class="product-name">Korvane Cap</h3>
    <div class="size-picker"><span>S</span><span class="is-selected">M</span><span>L</span></div>
    <p class="product-desc">Soft cotton twill with a curved brim and an adjustable strap at the back. Breathable panels keep you cool through every inning, and the clean stitched finish looks right in the stands, at practice, on the road or out on the street with friends after the game.</p>
    <div class="product-foot">
      <span class="price">999 $</span>
      <div class="qty"><span>−</span><span class="qty-box">1</span><span>+</span></div>
      <svg class="add-cart" width="16" height="16" viewBox="0 0 18 18" aria-label="Add to cart"><path d="M0 2h3l2.5 9h9.5l2-7H5" fill="none" stroke="#b3132e" stroke-width="2"/><path d="M5 5h11l-1.6 5.5H6.5z" fill="#b3132e"/><circle cx="7" cy="15.5" r="1.6" fill="#b3132e"/><circle cx="14" cy="15.5" r="1.6" fill="#b3132e"/></svg>
    </div>
  </article>

</div>
</body>
</html>
```